Professionell und kommunikativ, kommen gerne wieder.
Zielgruppe
Wir transportieren Güter und Waren aller Art rund um die Welt. Hauptsächlich Luftfracht, aber auch per Schiff und an Land. Hauptsächlich richten wir uns damit an Firmenkunden, weniger an Privatkunden. Für unsere neue Website benötigen wir ein Design.
Aufgabenstellung
Wir benötigen ein Webdesign für den Relaunch unserer Website. Unsere Ideen für unsere neue Website haben wir bereits skizziert (Anlage). Diese Mockups bedürfen nun eines Designs.
Dazu ergänzend gelten die folgenden, formalen Vorgaben:
• 1140px breit, gerne auch Ideen für die Darstellung auf Smartphones und Tablets
• Logo links oben
• Navigation oben waagerecht
• Dropdown-Navigation am Desktop, Hamburger für die mobile Navigation
• Verwendung eines Grid-Systems wie Bootstrap
• Mindestschriftgröße für Mengentext: 16px (bei groß ausfallenden Fonts 15px)
Wir haben keine Hausschriftart und keine festgelegten Farben. Wir möchten aber unser Logo weiterverwenden und da bietet es sich natürlich an, auf dem Rot aufzubauen.

```html
<!DOCTYPE html>
<html lang="de">
<head>
<meta charset="utf-8">
<title>SkyLoad – Air Freight</title>
<link rel="stylesheet" href="https://fonts.googleapis.com/css2?family=Urbanist:wght@400;500;600;700;800&display=swap">
<style>
:root{
  --red:#c41f30;
  --ink:#111418;
  --text:#3b3f46;
  --muted:#6b7079;
  --line:#e4e6ea;
  --soft:#f3f4f6;
  --dark:#25282b;
  --white:#ffffff;
  --stage:#fafafa;
}
*{box-sizing:border-box;margin:0;padding:0}
html,body{width:1200px;height:2293px;overflow:hidden;background:var(--stage)}
body{font-family:"Urbanist",sans-serif;color:var(--ink)}
.stage{position:absolute;left:0;top:0;width:1348px;height:2577px;transform:scale(0.8902);transform-origin:0 0}
.page{position:absolute;left:147px;top:73px;width:1054px;background:var(--white)}
.wrap{width:818px;margin:0 auto;position:relative}
a{color:inherit;text-decoration:none}
.btn{display:inline-flex;align-items:center;justify-content:center;background:var(--red);color:var(--white);font-size:12px;font-weight:600;height:35px;padding:0 12px;white-space:nowrap}

.topbar{height:26px;background:var(--red);color:var(--white);font-size:11.5px;font-weight:500}
.topbar .wrap{display:flex;justify-content:space-between;align-items:center;height:26px}

.header{height:52px;border-bottom:1px solid var(--line)}
.header .wrap{display:flex;align-items:center;justify-content:space-between;height:52px}
.brand{display:flex;align-items:center;gap:6px;font-size:24px;font-weight:400;letter-spacing:-0.5px;color:#555a60}
.brand-dot{width:14px;height:14px;border-radius:50%;background:var(--red)}
.nav{display:flex;align-items:center;gap:15px;font-size:12px;font-weight:500}
.nav .drop{display:flex;align-items:center;gap:6px}

.hero{height:498px;position:relative;background:linear-gradient(100deg,#9b4131 0%,#a64a36 22%,#5f79a6 38%,#b9cde6 55%,#cfdcec 72%,#8fa8cc 100%)}
.hero-text{position:absolute;left:120px;top:312px;color:var(--white)}
.hero h1{font-size:34px;font-weight:800;letter-spacing:-0.3px;margin-bottom:16px}
.hero p{font-size:14.5px;line-height:22px;width:300px;margin-bottom:22px}

.intro{height:192px}
.intro .wrap{display:flex;gap:28px;padding-top:62px}
.intro-item{width:254px}
.intro-item h3{font-size:15px;font-weight:600;margin-bottom:11px}
.intro-item p{font-size:11.5px;line-height:17.5px;color:var(--muted)}

.services{height:700px;background:var(--soft);padding-top:48px;text-align:center}
.eyebrow{font-size:11px;font-weight:600;letter-spacing:1px;color:var(--red)}
.services h2{font-size:27px;font-weight:700;margin-top:8px}
.cards{display:grid;grid-template-columns:repeat(3,261px);gap:18px;margin-top:45px;text-align:left}
.card{background:var(--white);height:232px;border-radius:4px;padding:17px 14px 17px 18px}
.card-icon{width:34px;height:34px;border-radius:50%;background:#fbe9eb;display:flex;align-items:center;justify-content:center}
.card h3{font-size:15.5px;font-weight:600;margin:19px 0 9px}
.card p{font-size:11.3px;line-height:17.7px;color:var(--muted);height:71px}
.card .btn{margin-top:15px}

.faq{height:622px;padding-top:72px;text-align:center}
.faq h2{font-size:27px;font-weight:700;letter-spacing:-0.3px}
.faq .lead{font-size:14.5px;color:var(--muted);margin-top:9px}
.faq-list{width:564px;margin:44px auto 0;text-align:left}
.faq-item{border-bottom:1px solid var(--line);display:flex;justify-content:space-between;align-items:flex-start;padding:21px 0 20px}
.faq-item:first-child{padding-top:0}
.faq-item:last-child{border-bottom:0}
.faq-item h4{font-size:13px;font-weight:500}
.faq-item p{font-size:11px;line-height:17.5px;color:var(--muted);margin-top:9px;width:520px}

.footer{height:167px;background:var(--dark);color:#e6e7e9;font-size:11.5px}
.footer .wrap{display:flex;padding-top:38px}
.company{width:325px;line-height:17.5px}
.company strong{font-weight:700;display:block}
.contact{display:flex;align-items:center;gap:9px;margin-top:8px}
.col{width:132px}
.col h5{font-size:11.5px;font-weight:700;margin-bottom:9px}
.col li{list-style:none;line-height:20.5px;white-space:nowrap}
.bottombar{height:26px;background:var(--red);color:#f4cfd3;font-size:11px;display:flex;align-items:center;justify-content:center}
</style>
</head>
<body>
<div class="stage">
<div class="page">

  <div class="topbar"><div class="wrap">
    <span>Tel: +00 12345 67890 (call us anytime)</span>
    <span>info@skyload-cargo.example</span>
  </div></div>

  <header class="header"><div class="wrap">
    <a class="brand" href="#"><span>SKYLOAD</span><span class="brand-dot"></span></a>
    <nav class="nav">
      <a href="#">Home</a>
      <a class="drop" href="#">Services
        <svg width="8" height="5" viewBox="0 0 8 5"><path d="M1 1l3 3 3-3" fill="none" stroke="#111418" stroke-width="1.1"/></svg></a>
      <a href="#">About Us</a>
      <a href="#">Contact</a>
      <a class="btn" href="#">Get a quote</a>
    </nav>
  </div></header>

  <section class="hero" role="img" aria-label="Passenger jet flying over stacked red and blue shipping containers under a blue sky">
    <div class="hero-text">
      <h1>Air Freight</h1>
      <p>Lorem ipsum dolor sit amet consectetur. Amet libero habitasse dui etiam pharetra augue.</p>
      <a class="btn" href="#">Get a quote</a>
    </div>
  </section>

  <section class="intro"><div class="wrap">
    <div class="intro-item"><h3>Who we are</h3><p>Lorem ipsum dolor sit amet consectetur. Non sodales arcu ut volutpat scelerisque diam</p></div>
    <div class="intro-item"><h3>Why Us</h3><p>Lorem ipsum dolor sit amet consectetur. Suspendisse etiam aliquam</p></div>
    <div class="intro-item"><h3>Air Freight</h3><p>Lorem ipsum dolor sit amet consectetur. Arcu mi mauris congue et natoque faucibus nisi</p></div>
  </div></section>

  <section class="services"><div class="wrap">
    <div class="eyebrow">SERVICES</div>
    <h2>Our Services</h2>
    <div class="cards">
      <div class="card">
        <div class="card-icon"><svg width="16" height="16" viewBox="0 0 16 16"><rect x="2.5" y="4" width="11" height="9" rx="1" fill="none" stroke="#c41f30" stroke-width="1.3"/><path d="M2.5 7h11M6.5 4v3" stroke="#c41f30" stroke-width="1.3" fill="none"/></svg></div>
        <h3>Import</h3>
        <p>Lorem ipsum dolor sit amet consectetur. At elementum mauris metus ullamcorper nec. Ac sit duis enim rhoncus tristique posuere tincidunt.</p>
        <a class="btn" href="#">Get a quote</a>
      </div>
      <div class="card">
        <div class="card-icon"><svg width="16" height="16" viewBox="0 0 16 16"><path d="M6 6V4a2 2 0 1 0-2 2h8a2 2 0 1 0-2-2v8a2 2 0 1 0 2-2H4a2 2 0 1 0 2 2V6z" fill="none" stroke="#c41f30" stroke-width="1.3"/></svg></div>
        <h3>Export</h3>
        <p>Lorem ipsum dolor sit amet consectetur. Tincidunt aliquet condimentum massa gravida enim vel viverra. Vel sapien ultricies in ullamcorper semper a.</p>
        <a class="btn" href="#">Get a quote</a>
      </div>
      <div class="card">
        <div class="card-icon"><svg width="16" height="16" viewBox="0 0 16 16"><path d="M8 2.5a5.5 5.5 0 0 1 0 11c-1 0-1.9-.2-2.7-.7L2.5 13.5l.7-2.8A5.5 5.5 0 0 1 8 2.5z" fill="none" stroke="#c41f30" stroke-width="1.3" stroke-linejoin="round"/></svg></div>
        <h3>Warehousing</h3>
        <p>Lorem ipsum dolor sit amet consectetur. Pellentesque libero ut vitae pellentesque sit aliquam et commodo adipiscing. Urna neque cursus vel.</p>
        <a class="btn" href="#">Get a quote</a>
      </div>
      <div class="card">
        <div class="card-icon"><svg width="16" height="16" viewBox="0 0 16 16"><rect x="2.5" y="4" width="11" height="9" rx="1" fill="none" stroke="#c41f30" stroke-width="1.3"/><path d="M2.5 7h11M6.5 4v3" stroke="#c41f30" stroke-width="1.3" fill="none"/></svg></div>
        <h3>Import</h3>
        <p>Lorem ipsum dolor sit amet consectetur. At elementum mauris metus ullamcorper nec. Ac sit duis enim rhoncus tristique posuere tincidunt.</p>
        <a class="btn" href="#">Get a quote</a>
      </div>
      <div class="card">
        <div class="card-icon"><svg width="16" height="16" viewBox="0 0 16 16"><path d="M6 6V4a2 2 0 1 0-2 2h8a2 2 0 1 0-2-2v8a2 2 0 1 0 2-2H4a2 2 0 1 0 2 2V6z" fill="none" stroke="#c41f30" stroke-width="1.3"/></svg></div>
        <h3>Export</h3>
        <p>Lorem ipsum dolor sit amet consectetur. Tincidunt aliquet condimentum massa gravida enim vel viverra. Vel sapien ultricies in ullamcorper semper a.</p>
        <a class="btn" href="#">Get a quote</a>
      </div>
      <div class="card">
        <div class="card-icon"><svg width="16" height="16" viewBox="0 0 16 16"><path d="M8 2.5a5.5 5.5 0 0 1 0 11c-1 0-1.9-.2-2.7-.7L2.5 13.5l.7-2.8A5.5 5.5 0 0 1 8 2.5z" fill="none" stroke="#c41f30" stroke-width="1.3" stroke-linejoin="round"/></svg></div>
        <h3>Warehousing</h3>
        <p>Lorem ipsum dolor sit amet consectetur. Pellentesque libero ut vitae pellentesque sit aliquam et commodo adipiscing. Urna neque cursus vel.</p>
        <a class="btn" href="#">Get a quote</a>
      </div>
    </div>
  </div></section>

  <section class="faq">
    <h2>Frequently asked questions</h2>
    <p class="lead">Everything you need to know about the product and billing.</p>
    <div class="faq-list">
      <div class="faq-item">
        <div><h4>Is there a free trial available?</h4>
        <p>Yes, you can try us for free for 30 days. If you want, we’ll provide you with a free, personalized 30-minute onboarding call to get you up and running as soon as possible.</p></div>
        <svg width="18" height="18" viewBox="0 0 18 18"><circle cx="9" cy="9" r="7.5" fill="none" stroke="#c41f30" stroke-width="1.3"/><path d="M5.5 9h7" stroke="#c41f30" stroke-width="1.3"/></svg>
      </div>
      <div class="faq-item"><h4>Can I change my plan later?</h4>
        <svg width="18" height="18" viewBox="0 0 18 18"><circle cx="9" cy="9" r="7.5" fill="none" stroke="#c41f30" stroke-width="1.3"/><path d="M5.5 9h7M9 5.5v7" stroke="#c41f30" stroke-width="1.3"/></svg></div>
      <div class="faq-item"><h4>What is your cancellation policy?</h4>
        <svg width="18" height="18" viewBox="0 0 18 18"><circle cx="9" cy="9" r="7.5" fill="none" stroke="#c41f30" stroke-width="1.3"/><path d="M5.5 9h7M9 5.5v7" stroke="#c41f30" stroke-width="1.3"/></svg></div>
      <div class="faq-item"><h4>Can other info be added to an invoice?</h4>
        <svg width="18" height="18" viewBox="0 0 18 18"><circle cx="9" cy="9" r="7.5" fill="none" stroke="#c41f30" stroke-width="1.3"/><path d="M5.5 9h7M9 5.5v7" stroke="#c41f30" stroke-width="1.3"/></svg></div>
      <div class="faq-item"><h4>How does billing work?</h4>
        <svg width="18" height="18" viewBox="0 0 18 18"><circle cx="9" cy="9" r="7.5" fill="none" stroke="#c41f30" stroke-width="1.3"/><path d="M5.5 9h7M9 5.5v7" stroke="#c41f30" stroke-width="1.3"/></svg></div>
      <div class="faq-item"><h4>How do I change my account email?</h4>
        <svg width="18" height="18" viewBox="0 0 18 18"><circle cx="9" cy="9" r="7.5" fill="none" stroke="#c41f30" stroke-width="1.3"/><path d="M5.5 9h7M9 5.5v7" stroke="#c41f30" stroke-width="1.3"/></svg></div>
    </div>
  </section>

  <footer class="footer"><div class="wrap">
    <div class="company">
      <strong>SkyLoad GmbH</strong>
      Lindenallee 14<br>00000 Beispielstadt
      <div class="contact"><svg width="14" height="14" viewBox="0 0 14 14"><path d="M3 1.5l2 .3 1 2.7-1.3 1a7 7 0 0 0 3.8 3.8l1-1.3 2.7 1 .3 2c-.1.6-.6 1-1.2 1A10.5 10.5 0 0 1 1.5 2.7c0-.6.4-1.1 1.5-1.2z" fill="none" stroke="#e6e7e9" stroke-width="1.1" stroke-linejoin="round"/></svg>+00 1234 5678900</div>
      <div class="contact"><svg width="14" height="14" viewBox="0 0 14 14"><rect x="1.5" y="3" width="11" height="8.5" rx="1" fill="none" stroke="#e6e7e9" stroke-width="1.1"/><path d="M1.8 3.5L7 7.5l5.2-4" fill="none" stroke="#e6e7e9" stroke-width="1.1"/></svg>info@skyload-cargo.example</div>
    </div>
    <div class="col"><h5>Navigation</h5><ul><li>Home</li><li>Services</li><li>About Us</li><li>Contact</li></ul></div>
    <div class="col"><h5>Services</h5><ul><li>Air Freight</li><li>Sea Freight</li><li>Land Transport</li><li>Airland Services</li></ul></div>
    <div class="col"><h5>Help</h5><ul><li>Help Center</li><li>FAQ</li></ul></div>
    <div class="col"><h5>Legal</h5><ul><li>Legal Notice</li><li>Term of Use</li><li>Privacy Statement</li></ul></div>
  </div></footer>
  <div class="bottombar">© 2022 SkyLoad. All Rights Reserved.</div>

</div>
</div>
</body>
</html>
```